Business card design needed

Business Card design required for new small plumbing business.
Would like a logo/text look that is simple and unique and does not have to be representative of a plumbing company (ie. having a cartoon plumber or toilet etc) as the companyname is self explanatory.
Would like the main colour to be green (lime green).

Industry/Entity Type

Plumber

Contact Information for Business Card

BRISCOMB PLUMBING
ABN 61 947 205 318 004

Harold Tenfield
Licensed Plumber 71635
Phone: 0477 261 408

27 Worrell Drive,
Fernbrook. 3987 Eastshire

Email: briscombplumbing@mailora.net

Logo Text

Briscomb Plumbing

Logo styles of interest
Character Logo
Wordmark Logo
Lettermark Logo

```html
<!DOCTYPE html>
<html lang="en">
<head>
<meta charset="utf-8">
<title>Briscomb Plumbing – Business Card</title>
<link rel="stylesheet" href="https://fonts.googleapis.com/css2?family=Exo+2:wght@400;500&display=swap">
<style>
  :root {
    --page-bg: #2a2a2a;
    --card-bg: #f7f7f7;
    --card-shade: #e4e4e4;
    --lime: #8cc43f;
    --lime-soft: #a9cf68;
    --ink: #1e1e1e;
    --icon-ring: #2b3a16;
  }
  * { box-sizing: border-box; margin: 0; padding: 0; }
  html, body { width: 1200px; height: 900px; overflow: hidden; }
  body {
    background: var(--page-bg);
    position: relative;
    font-family: "Exo 2", sans-serif;
  }
  .card {
    position: absolute;
    left: 320px;
    width: 560px;
    height: 320px;
    background: linear-gradient(160deg, var(--card-bg) 40%, var(--card-shade) 100%);
    box-shadow: 0 10px 30px rgba(0,0,0,.5);
  }
  .card--front { top: 70px; display: flex; align-items: center; justify-content: center; }
  .card--back { top: 510px; }
  .brand-name {
    font-weight: 400;
    font-size: 40px;
    letter-spacing: 2px;
    color: var(--lime-soft);
    white-space: nowrap;
  }
  .holder {
    position: absolute;
    right: 34px;
    top: 34px;
    text-align: right;
  }
  .holder__name {
    font-weight: 500;
    font-size: 36px;
    letter-spacing: 2px;
    color: var(--lime);
    line-height: 1;
    white-space: nowrap;
  }
  .holder__licence {
    font-size: 15px;
    letter-spacing: .5px;
    color: var(--lime);
    margin-top: 4px;
  }
  .contacts {
    position: absolute;
    left: 30px;
    bottom: 30px;
    list-style: none;
    font-size: 14px;
    letter-spacing: .3px;
    color: var(--ink);
  }
  .contacts li { display: flex; align-items: center; gap: 12px; height: 28px; white-space: nowrap; }
  .contacts svg { width: 20px; height: 20px; flex: none; }
</style>
</head>
<body>
  <section class="card card--front" aria-label="Card front">
    <h1 class="brand-name">BRISCOMB PLUMBING</h1>
  </section>

  <section class="card card--back" aria-label="Card back">
    <div class="holder">
      <h2 class="holder__name">HAROLD TENFIELD</h2>
      <p class="holder__licence">Licensed Plumber 71635</p>
    </div>
    <ul class="contacts">
      <li>
        <svg viewBox="0 0 20 20" aria-hidden="true">
          <circle cx="10" cy="10" r="9" fill="var(--lime)" stroke="var(--icon-ring)" stroke-width="1.5"/>
          <path d="M7 5.5 l1.6 2.4 -1 1 a6 6 0 0 0 3.5 3.5 l1-1 2.4 1.6 -1 1.6 c-3.5 .2 -7.5 -3.8 -7.3 -7.3z" fill="#fff"/>
        </svg>
        <span>0477 261 408</span>
      </li>
      <li>
        <svg viewBox="0 0 20 20" aria-hidden="true">
          <circle cx="10" cy="10" r="9" fill="var(--lime)" stroke="var(--icon-ring)" stroke-width="1.5"/>
          <path d="M10 5 L5 9.5 H6.5 V14.5 H9 V11.5 H11 V14.5 H13.5 V9.5 H15 Z" fill="#fff"/>
        </svg>
        <span>27 Worrell Drive, Fernbrook. 3987 Eastshire</span>
      </li>
      <li>
        <svg viewBox="0 0 20 20" aria-hidden="true">
          <circle cx="10" cy="10" r="9" fill="var(--lime)" stroke="var(--icon-ring)" stroke-width="1.5"/>
          <rect x="5.5" y="7" width="9" height="6.5" fill="#fff"/>
          <path d="M5.5 7 L10 10.5 L14.5 7" fill="none" stroke="var(--lime)" stroke-width="1"/>
        </svg>
        <span>briscombplumbing@mailora.net</span>
      </li>
    </ul>
  </section>
</body>
</html>
```